Home Services- Spring Clean Options

Brightwell Crew provides a variety of Home Services- focused on cleaning & improving the exterior of the home:

 Power Washing- driveways, sidewalks, patios, decks, fence
 Fence Staining- make fence look new with variety of staining colors
 Gutter cleaning- important to make sure have proper Water Drainage
 Gutter Guard Installation- prevent damage to roof and house by keeping debris out of gutters and water flowing.
 Window Washing- our exterior washing team and reach the highest windows
 Landscape& Patio Lights- highlight areas for beauty and safety
Updates

We are are almost finished. Just please make sure you pay attention to the wording and grammer in Red thx

Target Market(s)

Middle to Upper level Home Owners (especially women)

Industry/Entity Type

Cleaning Services

Font styles to use
Serif
Sans Serif

Requirements
Must have
• Not be Cluttered- Clean friendly, professional look. Focus on the Professional

Info@GoBrightwellCrew.com
972-648-0000
Nice to have
• Pictures of services- these are just examples
Should not have
• Bigger and bolder Services & Specials. Want to Show all the Services we offer but do Not use too much detail- don't want it to look "cluttered"

```html
<!DOCTYPE html>
<html lang="en">
<head>
<meta charset="utf-8">
<title>Brightwell Crew – Home Services Spring Clean</title>
<link rel="stylesheet" href="https://fonts.googleapis.com/css2?family=Barlow+Semi+Condensed:wght@300;500;700&family=Open+Sans:wght@400;600&display=swap">
<style>
  :root {
    --navy: #113d6f;
    --navy-deep: #0c2f59;
    --blue: #1f6fb4;
    --sky: #4aa3dc;
    --yellow: #fff200;
    --yellow-deep: #f4d800;
    --ink: #222a33;
    --label: #173f73;
    --white: #ffffff;
    --page: #eeeeee;
  }
  * { box-sizing: border-box; margin: 0; padding: 0; }
  html, body { width: 1200px; height: 1000px; overflow: hidden; background: var(--page); }
  .flyer {
    position: absolute; left: 284px; top: 57px;
    width: 625px; height: 882px;
    background: var(--white); overflow: hidden;
  }
  .flyer-art { position: absolute; left: 0; top: 0; }
  .headline {
    position: absolute; left: 38px; top: 34px;
    font-family: "Barlow Semi Condensed", sans-serif; font-weight: 700;
    line-height: 0.98; letter-spacing: 0.3px;
  }
  .headline .line-one { display: block; color: var(--white); font-size: 57px; }
  .headline .line-two {
    display: block; font-size: 74px;
    background: linear-gradient(180deg, var(--yellow) 30%, var(--yellow-deep) 100%);
    -webkit-background-clip: text; background-clip: text; color: transparent;
  }
  .intro {
    position: absolute; left: 40px; top: 350px;
    font-family: "Barlow Semi Condensed", sans-serif; color: var(--white);
  }
  .intro .company { font-weight: 300; font-size: 27px; letter-spacing: 0.2px; line-height: 1; }
  .intro .offer {
    color: var(--yellow); font-weight: 700; font-size: 29px;
    line-height: 1.05; margin-top: 3px;
  }
  .intro .focus { font-weight: 500; font-size: 17px; line-height: 1.3; margin-top: 10px; }
  .services { position: absolute; left: 0; top: 522px; width: 625px; list-style: none; }
  .services::before {
    content: ""; position: absolute; left: 63px; top: 26px; width: 2px; height: 258px;
    background: var(--blue);
  }
  .service {
    position: absolute; left: 40px; display: flex; align-items: center;
    font-family: "Open Sans", sans-serif; font-size: 14.5px; color: var(--ink); line-height: 1.42;
  }
  .service .icon { flex: 0 0 46px; width: 46px; height: 46px; }
  .service p { margin-left: 26px; width: 490px; }
  .service strong { color: var(--label); font-weight: 600; }
  .contact-bar {
    position: absolute; left: 0; top: 838px; width: 625px; height: 44px;
    background: linear-gradient(180deg, var(--blue) 0%, var(--navy-deep) 100%);
    display: flex; align-items: center; justify-content: center;
    font-family: "Open Sans", sans-serif; font-size: 14.5px; color: var(--white);
    white-space: nowrap;
  }
  .contact-item { display: flex; align-items: center; gap: 8px; padding: 0 13px; white-space: nowrap; }
  .contact-item svg { width: 17px; height: 17px; flex: 0 0 17px; }
  .divider { width: 2px; height: 26px; background: var(--sky); flex: 0 0 2px; }
</style>
</head>
<body>
<div class="flyer">
  <svg class="flyer-art" width="625" height="520" viewBox="0 0 625 520">
    <defs>
      <linearGradient id="gardenTone" x1="0" y1="0" x2="1" y2="1">
        <stop offset="0" stop-color="#5b6b4a"/>
        <stop offset="0.45" stop-color="#7e8c6a"/>
        <stop offset="0.75" stop-color="#8f8574"/>
        <stop offset="1" stop-color="#a88074"/>
      </linearGradient>
      <linearGradient id="skyBand" x1="0" y1="0" x2="0" y2="1">
        <stop offset="0" stop-color="#6cc0ee"/>
        <stop offset="1" stop-color="#1f78c0"/>
      </linearGradient>
      <linearGradient id="navyPanel" x1="0" y1="0" x2="0" y2="1">
        <stop offset="0" stop-color="#123f73"/>
        <stop offset="1" stop-color="#0c2f59"/>
      </linearGradient>
      <linearGradient id="windowTone" x1="0" y1="0" x2="1" y2="1">
        <stop offset="0" stop-color="#d9dde2"/>
        <stop offset="1" stop-color="#8f9aa6"/>
      </linearGradient>
      <linearGradient id="patioTone" x1="0" y1="0" x2="0" y2="1">
        <stop offset="0" stop-color="#4f7a3a"/>
        <stop offset="1" stop-color="#9a9488"/>
      </linearGradient>
    </defs>
    <rect width="625" height="360" fill="url(#gardenTone)" role="img" aria-label="Photo: worker power washing a garden patio"/>
    <path d="M0 250 C140 218 300 236 470 305 L470 430 L0 430 Z" fill="url(#skyBand)"/>
    <path d="M0 300 C130 284 290 296 470 360 L470 430 L0 430 Z" fill="#9fd6f3" opacity="0.7"/>
    <path d="M0 322 C120 300 250 310 350 356 L350 482 Q350 510 320 510 L0 510 Z" fill="url(#navyPanel)"/>
    <circle cx="538" cy="423" r="117" fill="url(#patioTone)" stroke="#fff200" stroke-width="6" role="img" aria-label="Photo: family at an outdoor patio kitchen"/>
    <circle cx="394" cy="414" r="91" fill="url(#windowTone)" stroke="#fff200" stroke-width="6" role="img" aria-label="Photo: man washing an exterior window"/>
  </svg>

  <h1 class="headline">
    <span class="line-one">HOME SERVICES-</span>
    <span class="line-two">SPRING CLEAN</span>
  </h1>

  <div class="intro">
    <p class="company">BRIGHTWELL CREW</p>
    <p class="offer">PROVIDES A VARIETY<br>OF HOME SERVICES-</p>
    <p class="focus">FOCUSED ON CLEANING &amp; IMPROVING<br>THE EXTERIOR OF THE HOME:</p>
  </div>

  <ul class="services">
    <li class="service" style="top:3px">
      <svg class="icon" viewBox="0 0 46 46"><circle cx="23" cy="23" r="22" fill="#1f6fb4" stroke="#cfe4f5" stroke-width="2"/><rect x="15" y="13" width="8" height="18" rx="2" fill="none" stroke="#fff" stroke-width="2"/><path d="M23 17 H30 M19 31 V35" stroke="#fff" stroke-width="2"/><circle cx="30" cy="24" r="3" fill="none" stroke="#fff" stroke-width="2"/></svg>
      <p><strong>Power Washing</strong>- driveways, sidewalks, patios,<br>decks, fence</p>
    </li>
    <li class="service" style="top:56px">
      <svg class="icon" viewBox="0 0 46 46"><circle cx="23" cy="23" r="22" fill="#1f6fb4" stroke="#cfe4f5" stroke-width="2"/><path d="M12 26 Q23 12 34 26 Z" fill="none" stroke="#fff" stroke-width="2"/><path d="M14 30 H32 M17 26 V30 M23 22 V30 M29 26 V30" stroke="#fff" stroke-width="2"/></svg>
      <p><strong>Fence Staining</strong>- make fence look new with variety of staining colors</p>
    </li>
    <li class="service" style="top:104px">
      <svg class="icon" viewBox="0 0 46 46"><circle cx="23" cy="23" r="22" fill="#1f6fb4" stroke="#cfe4f5" stroke-width="2"/><rect x="13" y="13" width="20" height="20" fill="none" stroke="#fff" stroke-width="2"/><path d="M13 20 H33 M13 26 H33 M20 13 V33 M26 13 V33" stroke="#fff" stroke-width="1.5"/></svg>
      <p><strong>Gutter cleaning</strong>- important to make sure have proper Water Drainage</p>
    </li>
    <li class="service" style="top:156px">
      <svg class="icon" viewBox="0 0 46 46"><circle cx="23" cy="23" r="22" fill="#1f6fb4" stroke="#cfe4f5" stroke-width="2"/><path d="M11 18 H35 L31 30 H15 Z" fill="none" stroke="#fff" stroke-width="2"/><path d="M14 14 L32 22" stroke="#fff" stroke-width="2"/></svg>
      <p><strong>Gutter Guard Installation</strong>- prevent damage to roof and house by<br>keeping debris out of gutters and water flowing.</p>
    </li>
    <li class="service" style="top:208px">
      <svg class="icon" viewBox="0 0 46 46"><circle cx="23" cy="23" r="22" fill="#1f6fb4" stroke="#cfe4f5" stroke-width="2"/><rect x="13" y="12" width="20" height="22" fill="none" stroke="#fff" stroke-width="2"/><path d="M23 12 V34 M13 23 H33" stroke="#fff" stroke-width="1.5"/><path d="M18 30 L28 18" stroke="#fff" stroke-width="2"/></svg>
      <p><strong>Window Washing</strong>- our exterior washing team and reach the<br>highest windows</p>
    </li>
    <li class="service" style="top:260px">
      <svg class="icon" viewBox="0 0 46 46"><circle cx="23" cy="23" r="22" fill="#1f6fb4" stroke="#cfe4f5" stroke-width="2"/><path d="M15 14 H31 L26 20 H20 Z" fill="#fff"/><path d="M23 20 V34 M18 34 H28" stroke="#fff" stroke-width="2"/></svg>
      <p><strong>Landscape&amp; Patio Lights</strong>- highlight areas for beauty and safety</p>
    </li>
  </ul>

  <footer class="contact-bar">
    <span class="contact-item">
      <svg viewBox="0 0 24 24"><path d="M6 3 L10 7 L8 10 Q10 14 14 16 L17 14 L21 18 L18 21 Q9 20 3 6 Z" fill="#fff200"/></svg>
      <span>972-648-0000</span>
    </span>
    <span class="divider"></span>
    <span class="contact-item">
      <svg viewBox="0 0 24 24"><rect x="2" y="5" width="20" height="14" fill="#fff200"/><path d="M2 5 L12 13 L22 5" fill="none" stroke="#0c2f59" stroke-width="1.5"/></svg>
      <span>Info@GoBrightwellCrew.com</span>
    </span>
    <span class="divider"></span>
    <span class="contact-item">
      <svg viewBox="0 0 24 24"><circle cx="12" cy="12" r="9" fill="none" stroke="#fff200" stroke-width="2"/><ellipse cx="12" cy="12" rx="4" ry="9" fill="none" stroke="#fff200" stroke-width="1.5"/><path d="M3 12 H21 M5 7 H19 M5 17 H19" stroke="#fff200" stroke-width="1.5"/></svg>
      <span>www.gobrightwellcrew.com</span>
    </span>
  </footer>
</div>
</body>
</html>
```